Option Sheet

We need a one page option sheet with a left to right reading of the five options. It should be a one sheet, multiple colors and definitive separations between options This is used in a sales consultation. Backround or colors not in option need to have the follow RGB value (5 red, 20 green, 63 blue)

We added a smaller text file, please change that point

Target Market(s)

Divorce

Industry/Entity Type

Legal

Requirements
Must have
• 1) All five options left to right
• 2)language included in sheet

```html
<!DOCTYPE html>
<html lang="en">
<head>
<meta charset="utf-8">
<title>Five Options | Divorce</title>
<link href="https://fonts.googleapis.com/css2?family=Roboto+Condensed:wght@700&family=Arimo:wght@400;700&display=swap" rel="stylesheet">
<style>
  :root {
    --page-bg: #f1f1f1;
    --sheet-bg: #ffffff;
    --ink: #14161c;
    --body-ink: #2e2e2e;
    --cross: #e3201b;
    --purple-a: #5c22a4; --purple-b: #7d3cb8; --purple-line: #7a2fb0;
    --blue-a: #0a63dc;   --blue-b: #25b2ec;   --blue-line: #1d8fd8;
    --teal-a: #05615d;   --teal-b: #0e8a7d;   --teal-line: #0b7a70;
    --green-a: #45ac2f;  --green-b: #9ad81e;  --green-line: #5cb832;
    --orange-a: #f28c18; --orange-b: #fde62c; --orange-line: #f4a21c;
  }
  * { box-sizing: border-box; margin: 0; padding: 0; }
  html, body { width: 1200px; height: 1000px; overflow: hidden; background: var(--page-bg); }
  .sheet {
    position: absolute; left: 250px; top: 15px; width: 742px; height: 975px;
    background: var(--sheet-bg);
  }
  .sheet-title {
    position: absolute; top: 38px; left: 0; width: 100%; text-align: center;
    font: 700 33px/1 "Roboto Condensed", sans-serif; color: var(--ink);
  }
  .col-head {
    position: absolute; top: 114px; font: 700 21px/1 "Roboto Condensed", sans-serif;
    color: var(--ink); text-align: center;
  }
  .col-head.option { left: 21px; width: 157px; }
  .col-head.adv { left: 178px; width: 270px; }
  .col-head.dis { left: 450px; width: 270px; }

  .option-row {
    position: absolute; left: 21px; width: 698px; height: 159px;
    display: grid; grid-template-columns: 157px 270px 271px;
    border: 2px solid var(--line); border-left: none;
  }
  .row-1 { top: 145px; --line: var(--purple-line); --a: var(--purple-a); --b: var(--purple-b); }
  .row-2 { top: 305px; --line: var(--blue-line);   --a: var(--blue-a);   --b: var(--blue-b); }
  .row-3 { top: 465px; --line: var(--teal-line);   --a: var(--teal-a);   --b: var(--teal-b); }
  .row-4 { top: 625px; --line: var(--green-line);  --a: var(--green-a);  --b: var(--green-b); }
  .row-5 { top: 784px; --line: var(--orange-line); --a: var(--orange-a); --b: var(--orange-b); }

  .option-cell {
    position: relative; margin: -2px 0; overflow: hidden;
    background: linear-gradient(200deg, var(--b) 0%, var(--a) 100%);
    display: flex; flex-direction: column; align-items: center; justify-content: flex-end;
    padding-bottom: 18px;
  }
  .row-4 .option-cell { background: linear-gradient(160deg, var(--a) 0%, var(--b) 100%); }
  .row-5 .option-cell { background: linear-gradient(180deg, var(--a) 0%, var(--b) 100%); }

  .option-number {
    position: absolute; top: -17px; left: 50%; transform: translateX(-50%);
    width: 42px; height: 42px; border-radius: 50%; background: #fff;
    border: 2px solid var(--line);
    font: 700 18px/1 "Roboto Condensed", sans-serif; color: var(--a); text-align: center;
    padding-top: 18px;
  }
  .option-flag {
    position: absolute; top: 10px; left: 157px; width: 22px; height: 18px;
    background: var(--b); clip-path: polygon(0 0, 100% 50%, 0 100%);
  }
  .row-5 .option-flag { background: var(--orange-a); }
  .option-icon { width: 72px; height: 72px; margin-bottom: 8px; }
  .icon-slot {
    width: 62px; height: 62px; margin-bottom: 10px; border-radius: 8px;
    background: rgba(255,255,255,0.28);
  }
  .option-label {
    font: 700 17px/1.3 "Roboto Condensed", sans-serif; color: #fff; text-align: center;
    white-space: nowrap;
  }

  .adv-cell, .dis-cell { display: flex; align-items: center; }
  .adv-cell { padding: 0 4px 0 23px; }
  .dis-cell { border-left: 2px solid var(--line); padding: 0 6px 0 20px; }
  .point-list { list-style: none; font: 400 12px/1.25 "Arimo", sans-serif; color: var(--body-ink); }
  .point-list li { position: relative; padding-left: 18px; margin: 2px 0; }
  .dis-cell .point-list li { margin: 0 0 3px; }
  .point-list li.tight { white-space: nowrap; letter-spacing: -0.3px; }
  .pro::before {
    content: "\2713"; position: absolute; left: 0; top: -2px;
    font: 700 14px/1.2 "Arimo", sans-serif; color: var(--a);
  }
  .row-5 .pro::before { color: var(--orange-a); }
  .con::before {
    content: "\2717"; position: absolute; left: 0; top: -2px;
    font: 700 15px/1.2 "Arimo", sans-serif; color: var(--cross);
  }
</style>
</head>
<body>
<main class="sheet">
  <h1 class="sheet-title">FIVE OPTIONS | Divorce</h1>
  <div class="col-head option">OPTION</div>
  <div class="col-head adv">ADVANTAGES</div>
  <div class="col-head dis">DISADVANTAGES</div>

  <section class="option-row row-1">
    <div class="option-cell">
      <span class="option-number">1</span>
      <svg class="option-icon" viewBox="0 0 72 72" aria-hidden="true">
        <circle cx="36" cy="36" r="22" fill="none" stroke="#fff" stroke-width="6"/>
        <line x1="12" y1="66" x2="62" y2="6" stroke="#fff" stroke-width="6" stroke-linecap="round"/>
      </svg>
      <div class="option-label">DO NOTHING</div>
    </div>
    <span class="option-flag"></span>
    <div class="adv-cell"><ul class="point-list">
      <li class="pro">Stay married</li>
      <li class="pro">No life Changes</li>
    </ul></div>
    <div class="dis-cell"><ul class="point-list">
      <li class="con">Remain unhappy, depressed, anxious</li>
      <li class="con">Money and assets may disappear</li>
      <li class="con">What is going to change?</li>
    </ul></div>
  </section>

  <section class="option-row row-2">
    <div class="option-cell">
      <span class="option-number">2</span>
      <div class="icon-slot" role="img" aria-label="Icon of two people talking across a table"></div>
      <div class="option-label">GO TO<br>COUNSELLING</div>
    </div>
    <span class="option-flag"></span>
    <div class="adv-cell"><ul class="point-list">
      <li class="pro">Reconcile marriage</li>
      <li class="pro">Help make a better life</li>
    </ul></div>
    <div class="dis-cell"><ul class="point-list">
      <li class="con">Past issues are highlighted and may drudge up old wounds</li>
      <li class="con">It may just clarify the reasons you need to separate and/or divorce</li>
      <li class="con">Both parties must be invested and willing to participate</li>
    </ul></div>
  </section>

  <section class="option-row row-3">
    <div class="option-cell">
      <span class="option-number">3</span>
      <div class="icon-slot" role="img" aria-label="Briefcase icon"></div>
      <div class="option-label">DO IT YOURSELF</div>
    </div>
    <span class="option-flag"></span>
    <div class="adv-cell"><ul class="point-list">
      <li class="pro">No attorney fees</li>
      <li class="pro">You are your on attorney</li>
    </ul></div>
    <div class="dis-cell"><ul class="point-list">
      <li class="con">People often find that what is “fair,” may in fact, not be truly fair</li>
      <li class="con tight">Often times, people do not know the risks</li>
      <li>Complicated legal system within intrigue rules</li>
      <li class="con">Unsure how to complete the necessary paperwork and meet the deadlines</li>
    </ul></div>
  </section>

  <section class="option-row row-4">
    <div class="option-cell">
      <span class="option-number">4</span>
      <div class="icon-slot" role="img" aria-label="Icon of a person in a suit on the phone"></div>
      <div class="option-label">LIMITED<br>REPRESENTATION</div>
    </div>
    <span class="option-flag"></span>
    <div class="adv-cell"><ul class="point-list">
      <li class="pro">Balance between going alone and our limited involvement in the case</li>
    </ul></div>
    <div class="dis-cell"><ul class="point-list">
      <li class="con">Our terms may not benefit from our legal knowledge</li>
      <li class="con">The legal consequences of your legal documents will not be explained to you so that you can formulate a plan for handling the rest of your case.</li>
      <li class="con">Your spouse or other parties may cause your legal fees to increase significantly without action on your part</li>
    </ul></div>
  </section>

  <section class="option-row row-5">
    <div class="option-cell">
      <span class="option-number">5</span>
      <div class="icon-slot" role="img" aria-label="Handshake icon"></div>
      <div class="option-label">HIRE US!</div>
    </div>
    <span class="option-flag"></span>
    <div class="adv-cell"><ul class="point-list">
      <li class="pro tight">Gain the full benefits of our experience</li>
      <li class="pro tight">Have a team of Family Law focus attorneys</li>
      <li class="pro">Often saves you or makes you money in the long run</li>
      <li class="pro">Save you time, energy and stress</li>
    </ul></div>
    <div class="dis-cell"><ul class="point-list">
      <li class="con">Initial cost</li>
    </ul></div>
  </section>
</main>
</body>
</html>
```